New Hotel Showcase Website

We plan to launch a website called www.brindlestays.net which showcases the world’s best new hotels. We want a mock up for 2 pages: the homepage (page 1) and the individual hotel page (page 2). We are looking for a design which combines simplicity while highlighting images/features of the hotel. Because the theme of the site is new hotels it is important that the design somehow emphasizes the age of each hotel listed – both on the homepage and then on the individual hotel page.

NOTE: WE WANT A CREATIVE, NEW APPROACH TO DISPLAYING HOTELS. NOT JUST A COPY OF CURRENT HOTEL WEBSITES.

The design should consider unique and creative ways of helping users to navigate the homepage (page 1) based on the age, location or style of the hotel they are interested in. The individual hotel page(page 2) can be more standard by clearly setting out hotel photos, feature lists, reviews, contact details and potential discounts. There is no booking system needed as this is not a hotel booking website.

The design should ideally be compatible with a content management system such as Page Loom. In terms of reference materials we like sites similar to:

http://www.velmarquay.net
http://www.corvidandpine.net
http://www.tessarooms.net
http://www.quillbeds.net

These sites are designed far more simply than large booking sites such as www.roamvix.net, www.bunkfold.net or even wander ledger. However, we are not looking for a copy of the above. We are looking for a design that presents hotels in a novel way and would be seen by the industry as a unique way of displaying new hotels.
Updates

Dear Designers - we have received quite a few entries already. Thank you. However, none of the designs submitted have responded to our brief. They are all copies or derivatives of current hotel websites which is not what we are looking for. We want (a) a new and creative approach to a hotel website and (b) one which creatively uses the age of the hotel (ie. 1 month old, 6 months old etc).

It will require creative thinking and new ideas. We wanted to challenge designers to come up with something new. Thanks.

```html
<!DOCTYPE html>
<html lang="en">
<head>
<meta charset="utf-8">
<title>Brindlestays – Greece</title>
<link href="https://fonts.googleapis.com/css2?family=Roboto:ital,wght@0,300;0,400;0,500;1,300&display=swap" rel="stylesheet">
<style>
  :root {
    --ink: #231f20;
    --black: #000000;
    --white: #ffffff;
    --red: #cc0000;
    --panel: rgba(243, 244, 248, 0.93);
    --tab-active: #eceef3;
    --button-grey: #6a6a6a;
    --muted: #6b6b6b;
    --body-text: #333333;
    --sea-deep: #4a5f86;
    --sea-light: #8ea3c4;
    --wall-light: #e9ebee;
    --wall-shade: #a9acb1;
  }
  * { margin: 0; padding: 0; box-sizing: border-box; }
  html, body { width: 1200px; height: 2410px; overflow: hidden; }
  body { position: relative; font-family: "Roboto", Arial, sans-serif; background: var(--white); color: var(--ink); }

  .site-header { position: absolute; left: 0; top: 0; width: 1200px; height: 93px; background: var(--ink); }
  .brand { position: absolute; left: 100px; top: 34px; display: flex; align-items: center; gap: 10px; color: var(--white); font-weight: 300; font-size: 30px; letter-spacing: 1px; }
  .brand-mark { width: 14px; height: 22px; background: var(--red); }

  .hero-photo { position: absolute; left: 0; top: 93px; width: 1200px; height: 2171px;
    background:
      radial-gradient(ellipse 700px 900px at 250px 1800px, rgba(235,237,240,0.95), rgba(235,237,240,0) 70%),
      radial-gradient(ellipse 500px 800px at 1050px 1650px, rgba(200,203,208,0.85), rgba(200,203,208,0) 70%),
      linear-gradient(180deg, var(--sea-deep) 0%, var(--sea-light) 35%, #b8c4d6 55%, var(--wall-light) 75%, var(--wall-shade) 100%); }

  .page-title { position: absolute; left: 0; top: 185px; width: 1200px; text-align: center; color: var(--white); font-weight: 300; font-size: 100px; line-height: 1.2; }
  .intro { position: absolute; left: 237px; top: 406px; color: var(--white); font-weight: 300; font-size: 27px; }

  .age-tab { position: absolute; top: 477px; width: 203px; height: 203px; display: flex; align-items: center; justify-content: center; text-align: center; font-weight: 300; font-size: 52px; line-height: 1.2; background: var(--black); color: var(--white); }
  .age-tab.is-active { background: var(--tab-active); color: var(--black); }
  .tab-year { left: 234px; }
  .tab-months { left: 499px; }
  .tab-new { left: 764px; }

  .results-panel { position: absolute; left: 114px; top: 680px; width: 974px; height: 1377px; background: var(--panel); }

  .hotel-card { position: absolute; left: 58px; width: 880px; height: 280px; }
  .hotel-photo { position: absolute; left: 0; top: 0; width: 258px; height: 260px;
    background: linear-gradient(180deg, #2d63b3 0%, #3b6cb8 28%, #3e3a3a 45%, #5a4a3c 70%, #2f4d25 100%); }
  .birth-label { position: absolute; left: 0; top: 0; width: 258px; height: 65px; background: var(--red); color: var(--white); font-weight: 500; font-size: 24px; line-height: 29px; padding: 5px 0 0 9px; }
  .hotel-name { position: absolute; left: 274px; top: 0; color: var(--red); font-size: 29px; font-weight: 400; }
  .hotel-location { position: absolute; left: 274px; top: 40px; font-size: 24px; font-weight: 500; color: var(--black); }
  .map-button { position: absolute; left: 553px; top: 29px; width: 200px; height: 35px; background: var(--button-grey); color: var(--white); font-size: 24px; display: flex; align-items: center; gap: 8px; padding-left: 10px; }
  .info-heading { position: absolute; left: 274px; top: 74px; font-size: 26px; color: var(--black); }
  .info-text { position: absolute; left: 274px; top: 108px; width: 600px; font-size: 16px; line-height: 20.6px; color: var(--body-text); font-weight: 300; }
  .detail-link { position: absolute; left: 274px; top: 236px; font-size: 23px; font-style: italic; font-weight: 300; color: var(--muted); }

  .card-1 { top: 55px; } .card-2 { top: 370px; } .card-3 { top: 685px; } .card-4 { top: 1000px; }

  .show-more { position: absolute; left: 0; top: 1317px; width: 974px; text-align: center; color: var(--red); font-size: 24px; }

  .brand-new-note { position: absolute; left: 114px; top: 2087px; width: 974px; height: 69px; background: var(--black); color: var(--white); font-size: 29px; display: flex; align-items: center; justify-content: center; }
  .brand-new-note em { font-style: normal; color: var(--red); }

  .site-footer { position: absolute; left: 0; top: 2264px; width: 1200px; height: 146px; background: var(--black); color: var(--white); }
  .social-links { position: absolute; left: 0; top: 44px; width: 1200px; display: flex; justify-content: center; gap: 26px; font-size: 20px; font-weight: 500; }
  .copyright { position: absolute; left: 0; top: 122px; width: 1200px; text-align: center; font-size: 11px; }
</style>
</head>
<body>
  <header class="site-header">
    <div class="brand"><span>BRINDLESTAYS</span><span class="brand-mark"></span></div>
  </header>

  <div class="hero-photo" role="img" aria-label="Photo of whitewashed Greek island terrace and steps above a deep blue sea"></div>

  <h1 class="page-title">Greece it is then!</h1>
  <p class="intro">Now, let's find a hotel. Tell us what you are interested in.</p>

  <div class="age-tab tab-year is-active">1 year<br>old</div>
  <div class="age-tab tab-months">...<br>months<br>old</div>
  <div class="age-tab tab-new">only<br>brand<br>new</div>

  <main class="results-panel">
    <article class="hotel-card card-1">
      <div class="hotel-photo" role="img" aria-label="Hotel view over the Athens skyline at dusk"></div>
      <div class="birth-label">Date of birth:<br>October 2012</div>
      <h2 class="hotel-name">Athens Agora Court</h2>
      <p class="hotel-location">Location: Psirry, Athens</p>
      <span class="map-button">show on map <svg width="20" height="20" viewBox="0 0 20 20"><circle cx="12" cy="8" r="5.5" fill="none" stroke="#fff" stroke-width="2.5"/><line x1="8" y1="12" x2="2" y2="18" stroke="#fff" stroke-width="3"/></svg></span>
      <h3 class="info-heading">Hotel info:</h3>
      <p class="info-text">Lorem ipsum dolor sit amet, consectetur adipisicing elit, sed do eiusmod tempor incididunt ut labore et dolore magna aliqua. Ut enim ad minim veniam, quis nostrud exercitation ullamco laboris nisi ut aliquip ex ea commodo consequat. Duis aute irure dolor in reprehenderit in voluptate velit esse cillum dolore eu fugiat nulla pariatur. Excepteur sint occaecat cupidatat non proident, sunt in culpa qui officia deserunt mollit anim id est laborum.</p>
      <a class="detail-link">detailed presentation &gt;&gt;</a>
    </article>

    <article class="hotel-card card-2">
      <div class="hotel-photo" role="img" aria-label="Hotel view over the Athens skyline at dusk"></div>
      <div class="birth-label">Date of birth:<br>October 2012</div>
      <h2 class="hotel-name">Athens Agora Court</h2>
      <p class="hotel-location">Location: Psirry, Athens</p>
      <span class="map-button">show on map <svg width="20" height="20" viewBox="0 0 20 20"><circle cx="12" cy="8" r="5.5" fill="none" stroke="#fff" stroke-width="2.5"/><line x1="8" y1="12" x2="2" y2="18" stroke="#fff" stroke-width="3"/></svg></span>
      <h3 class="info-heading">Hotel info:</h3>
      <p class="info-text">Lorem ipsum dolor sit amet, consectetur adipisicing elit, sed do eiusmod tempor incididunt ut labore et dolore magna aliqua. Ut enim ad minim veniam, quis nostrud exercitation ullamco laboris nisi ut aliquip ex ea commodo consequat. Duis aute irure dolor in reprehenderit in voluptate velit esse cillum dolore eu fugiat nulla pariatur. Excepteur sint occaecat cupidatat non proident, sunt in culpa qui officia deserunt mollit anim id est laborum.</p>
      <a class="detail-link">detailed presentation &gt;&gt;</a>
    </article>

    <article class="hotel-card card-3">
      <div class="hotel-photo" role="img" aria-label="Hotel view over the Athens skyline at dusk"></div>
      <div class="birth-label">Date of birth:<br>October 2012</div>
      <h2 class="hotel-name">Athens Agora Court</h2>
      <p class="hotel-location">Location: Psirry, Athens</p>
      <span class="map-button">show on map <svg width="20" height="20" viewBox="0 0 20 20"><circle cx="12" cy="8" r="5.5" fill="none" stroke="#fff" stroke-width="2.5"/><line x1="8" y1="12" x2="2" y2="18" stroke="#fff" stroke-width="3"/></svg></span>
      <h3 class="info-heading">Hotel info:</h3>
      <p class="info-text">Lorem ipsum dolor sit amet, consectetur adipisicing elit, sed do eiusmod tempor incididunt ut labore et dolore magna aliqua. Ut enim ad minim veniam, quis nostrud exercitation ullamco laboris nisi ut aliquip ex ea commodo consequat. Duis aute irure dolor in reprehenderit in voluptate velit esse cillum dolore eu fugiat nulla pariatur. Excepteur sint occaecat cupidatat non proident, sunt in culpa qui officia deserunt mollit anim id est laborum.</p>
      <a class="detail-link">detailed presentation &gt;&gt;</a>
    </article>

    <article class="hotel-card card-4">
      <div class="hotel-photo" role="img" aria-label="Hotel view over the Athens skyline at dusk"></div>
      <div class="birth-label">Date of birth:<br>October 2012</div>
      <h2 class="hotel-name">Athens Agora Court</h2>
      <p class="hotel-location">Location: Psirry, Athens</p>
      <span class="map-button">show on map <svg width="20" height="20" viewBox="0 0 20 20"><circle cx="12" cy="8" r="5.5" fill="none" stroke="#fff" stroke-width="2.5"/><line x1="8" y1="12" x2="2" y2="18" stroke="#fff" stroke-width="3"/></svg></span>
      <h3 class="info-heading">Hotel info:</h3>
      <p class="info-text">Lorem ipsum dolor sit amet, consectetur adipisicing elit, sed do eiusmod tempor incididunt ut labore et dolore magna aliqua. Ut enim ad minim veniam, quis nostrud exercitation ullamco laboris nisi ut aliquip ex ea commodo consequat. Duis aute irure dolor in reprehenderit in voluptate velit esse cillum dolore eu fugiat nulla pariatur. Excepteur sint occaecat cupidatat non proident, sunt in culpa qui officia deserunt mollit anim id est laborum.</p>
      <a class="detail-link">detailed presentation &gt;&gt;</a>
    </article>

    <p class="show-more">show more</p>
  </main>

  <p class="brand-new-note">Not there yet? Perhaps you should check our&nbsp;<em>brand new</em>&nbsp;hotel section.</p>

  <footer class="site-footer">
    <nav class="social-links">
      <span>Chatterly</span>
      <span>Peepline</span>
      <span>Snapframe</span>
      <span>Pinboardly</span>
      <span>Reelcast</span>
    </nav>
    <p class="copyright">Copyright © 2013 BRINDLESTAYS - All Rights Reserved</p>
  </footer>
</body>
</html>
```